Lumigrove Pages with Bold Font

I want the font to be simple yet bold for Lumigrove images. Its all about a simple bold readable font. I need a single lumigrove page with an image and copy/text on or over the image. The words will change in the future. I'm looking for the right font. I like fiery red and yellow colors. The "One Pic" attached is a sample of what I want without the Velnor words.

```html
<!DOCTYPE html>
<html lang="en">
<head>
<meta charset="utf-8">
<title>Marla Quinn Vale – Trainer for Men</title>
<link rel="stylesheet" href="https://fonts.googleapis.com/css2?family=Anton&family=Josefin+Sans:wght@600&family=Poppins:wght@500&display=swap">
<style>
  :root {
    --red-deep: #3a0006;
    --red-mid: #a8001a;
    --red-bright: #ff0030;
    --yellow: #ffc400;
    --yellow-head: #ffd400;
    --brown-dark: #2a1510;
    --shadow-dark: #3b1f1a;
    --navy: #1d3558;
    --navy-light: #34557e;
    --white: #ffffff;
    --tan: #c98c62;
  }
  * { margin: 0; padding: 0; box-sizing: border-box; }
  html, body { width: 1200px; height: 1200px; overflow: hidden; background: var(--red-deep); }
  .post {
    position: relative;
    width: 1200px;
    height: 1200px;
    overflow: hidden;
    background: linear-gradient(90deg, var(--red-deep) 0%, var(--red-mid) 55%, var(--red-bright) 100%);
  }
  .trainer-photo {
    position: absolute;
    left: 0; top: 0;
    width: 620px; height: 1200px;
    background:
      radial-gradient(ellipse 55% 60% at 50% 55%, var(--tan) 0%, rgba(201,140,98,0.55) 45%, rgba(90,0,10,0) 75%),
      linear-gradient(90deg, #4a0008 0%, #6a000f 60%, rgba(120,0,20,0) 100%);
  }
  .shapes { position: absolute; inset: 0; width: 1200px; height: 1200px; }
  .name-block {
    position: absolute;
    left: 680px; top: 8px;
    width: 490px;
    text-align: center;
    color: var(--brown-dark);
  }
  .trainer-name {
    font-family: "Anton", sans-serif;
    font-size: 74px;
    line-height: 92px;
    letter-spacing: -0.5px;
    white-space: nowrap;
  }
  .trainer-role {
    font-family: "Josefin Sans", sans-serif;
    font-weight: 600;
    font-size: 48px;
    line-height: 48px;
    letter-spacing: 1px;
    white-space: nowrap;
  }
  .wanna {
    position: absolute;
    left: 700px; top: 476px;
    transform: translate(-50%, -50%) rotate(-90deg) skewX(-3deg);
    font-family: "Anton", sans-serif;
    font-size: 104px;
    line-height: 1;
    letter-spacing: 4px;
    color: var(--white);
    white-space: nowrap;
  }
  .headline {
    position: absolute;
    left: 776px; top: 266px;
    font-family: "Anton", sans-serif;
    font-size: 104px;
    line-height: 97px;
    color: var(--yellow-head);
    text-shadow: 3px 3px 0 rgba(60,0,0,0.45);
    white-space: nowrap;
  }
  .promise {
    position: absolute;
    left: 572px; top: 738px;
    font-family: "Anton", sans-serif;
    color: var(--white);
    white-space: nowrap;
    line-height: 1;
  }
  .promise .small { font-size: 94px; }
  .promise .big { font-size: 124px; }
  .pitch {
    position: absolute;
    left: 520px; right: 25px; top: 866px;
    font-family: "Poppins", sans-serif;
    font-weight: 500;
    font-size: 34px;
    line-height: 45px;
    color: var(--white);
    text-align: right;
  }
</style>
</head>
<body>
  <main class="post">
    <div class="trainer-photo" role="img" aria-label="Photo of the trainer posing in front of a dark red light-streaked backdrop"></div>

    <svg class="shapes" viewBox="0 0 1200 1200" aria-hidden="true">
      <polygon class="banner-shadow" points="648,0 666,256 1090,155 1200,0" fill="var(--shadow-dark)"/>
      <polygon class="banner" points="648,0 1200,0 1200,140 684,222" fill="var(--yellow)"/>
      <polygon class="tag-shadow" points="621,306 765,288 765,676 621,702" fill="#1a0a0a"/>
      <defs>
        <linearGradient id="tagFill" x1="0" y1="0" x2="0" y2="1">
          <stop offset="0" stop-color="var(--navy-light)"/>
          <stop offset="1" stop-color="#0f2340"/>
        </linearGradient>
      </defs>
      <polygon class="tag" points="636,296 765,280 765,651 636,667" fill="url(#tagFill)"/>
      <line x1="632" y1="298" x2="632" y2="668" stroke="var(--white)" stroke-width="3"/>
    </svg>

    <header class="name-block">
      <h1 class="trainer-name">MARLA QUINN VALE</h1>
      <p class="trainer-role">TRAINER FOR MEN</p>
    </header>

    <div class="wanna">WANNA</div>

    <h2 class="headline">LOOSE<br>WEIGHT?<br>SHRINK<br>THAT GUT?</h2>

    <p class="promise"><span class="small">I CAN </span><span class="big">HELP</span><span class="small"> YOU.</span></p>

    <p class="pitch">The sectret to find what works for you! And I can give you that. The pounds will melt away, your gut will shrink and your health will improve.</p>
  </main>
</body>
</html>
```